Design Business Card Aerial Drone Photography

we need a business card that shows we are a leader in:
-Aerial Videos
-Aerial Photography
-Aerial Real Estate Photography
the attached logo is in blue, however please feel free to submit creative colors and designs
Updates

I would like to add the words "Veteran Owned and Operated" to my business card Certified Drone Operator should appear as one line Thanks, Ned Corliss

Target Market(s)

real estate, cell towers, companies that want to showcase their company with aerial drone photography

Contact Information for Business Card

logo files have been submitted in pdf, jpg, png, .ai, .eps., .svg formats. Please feel free to be creative with design and colors, possibly a cloud type background
sample attached.
review my website www.brightwrenaerial.example that should help with designing my business card
Services:
-Aerial Videos
-Aerial Photography

Font styles to use
Sans Serif

Colors

Designer to choose colors to be used in the design.

Requirements
Must have
• company logo
• Bright Wren Aerial
• Ned Corliss Certified Drone Operator
• 555-619-4827
• brightwrenaerial@mailbox.example
• www.brightwrenaeriel.example
• 2971 Maplewood Ln, Dunwoody GA 30338
Nice to have
• Please feel free to be creative with design and colors

```html
<!DOCTYPE html>
<html lang="en">
<head>
<meta charset="utf-8">
<title>Bright Wren Aerial — Business Card</title>
<link rel="stylesheet" href="https://fonts.googleapis.com/css2?family=Roboto:wght@400;500;700&family=Roboto+Condensed:wght@700&display=swap">
<style>
  :root {
    --bg: #2b2b2d;
    --card: #1f1f21;
    --card-edge: #2a2a2c;
    --blue: #1a8fe0;
    --white: #f2f2f2;
    --muted: #6b6b6e;
  }
  * { box-sizing: border-box; margin: 0; padding: 0; }
  html, body { width: 1200px; height: 900px; overflow: hidden; }
  body {
    background: var(--bg);
    font-family: "Roboto", Arial, sans-serif;
    color: var(--white);
    position: relative;
  }
  .card {
    position: absolute;
    left: 280px;
    width: 640px;
    height: 366px;
    background: var(--card);
    border: 1px solid var(--card-edge);
    border-radius: 3px;
    box-shadow: 0 10px 28px rgba(0,0,0,.45);
  }
  .card--front { top: 66px; }
  .card--back { top: 462px; }

  /* Front */
  .brand {
    position: absolute;
    top: 82px; left: 0; right: 0;
    display: flex; align-items: center; justify-content: center; gap: 14px;
  }
  .brand__dot {
    width: 22px; height: 22px; border-radius: 50%;
    background: var(--blue);
  }
  .brand__name {
    font-family: "Roboto Condensed", "Roboto", sans-serif;
    font-weight: 700;
    font-size: 42px;
    color: var(--blue);
    letter-spacing: .5px;
    text-transform: uppercase;
  }
  .services {
    position: absolute; top: 220px; left: 0; right: 0; text-align: center;
  }
  .services__title {
    color: var(--blue); font-weight: 700; font-size: 20px;
    letter-spacing: .5px; margin-bottom: 10px;
  }
  .services__list {
    list-style: none; display: flex; justify-content: center; gap: 10px;
    font-size: 16px;
  }
  .services__list li + li::before {
    content: ""; display: inline-block; width: 6px; height: 6px;
    border-radius: 50%; background: var(--blue);
    margin-right: 10px; vertical-align: middle;
  }

  /* Back */
  .identity {
    position: absolute; top: 86px; right: 366px; text-align: right;
    text-transform: uppercase;
  }
  .identity__company {
    font-family: "Roboto Condensed", "Roboto", sans-serif;
    color: var(--blue); font-weight: 700; font-size: 24px; margin-bottom: 6px;
  }
  .identity__role { font-weight: 500; font-size: 17px; line-height: 1.3; }
  .divider {
    position: absolute; left: 290px; top: 78px; width: 1px; height: 96px;
    background: var(--muted);
  }
  .contacts {
    position: absolute; top: 100px; left: 316px; list-style: none;
    font-size: 16px;
  }
  .contacts li { display: flex; align-items: center; gap: 10px; margin-bottom: 8px; }
  .contacts svg, .address svg { flex: none; fill: var(--blue); }
  .address {
    position: absolute; top: 270px; left: 0; right: 0;
    display: flex; justify-content: center; align-items: center; gap: 8px;
    font-size: 18px;
  }
</style>
</head>
<body>
  <section class="card card--front" aria-label="Card front">
    <div class="brand">
      <span class="brand__dot"></span>
      <span class="brand__name">Bright Wren Aerial</span>
    </div>
    <div class="services">
      <h2 class="services__title">SERVICES:</h2>
      <ul class="services__list">
        <li>Aerial Videos</li>
        <li>Aerial Photography</li>
        <li>Aerial Real Estate Photography</li>
      </ul>
    </div>
  </section>

  <section class="card card--back" aria-label="Card back">
    <div class="identity">
      <p class="identity__company">Bright Wren Aerial</p>
      <p class="identity__role">Ned Corliss Certified<br>Drone Operator</p>
    </div>
    <div class="divider"></div>
    <ul class="contacts">
      <li>
        <svg width="16" height="16" viewBox="0 0 24 24" aria-hidden="true"><path d="M6.6 10.8a15 15 0 0 0 6.6 6.6l2.2-2.2a1 1 0 0 1 1-.25 11.4 11.4 0 0 0 3.6.57 1 1 0 0 1 1 1V20a1 1 0 0 1-1 1A17 17 0 0 1 3 4a1 1 0 0 1 1-1h3.5a1 1 0 0 1 1 1c0 1.25.2 2.450.57 3.57a1 1 0 0 1-.25 1z"/></svg>
        <span>555-619-4827</span>
      </li>
      <li>
        <svg width="16" height="16" viewBox="0 0 24 24" aria-hidden="true"><path d="M2 5h20v14H2z M2 5l10 8 10-8" /></svg>
        <span>brightwrenaerial@mailbox.example</span>
      </li>
      <li>
        <svg width="16" height="16" viewBox="0 0 24 24" aria-hidden="true"><circle cx="12" cy="12" r="10"/></svg>
        <span>www.brightwrenaeriel.example</span>
      </li>
    </ul>
    <p class="address">
      <svg width="16" height="20" viewBox="0 0 24 30" aria-hidden="true"><path d="M12 0a10 10 0 0 0-10 10c0 8 10 20 10 20s10-12 10-20A10 10 0 0 0 12 0zm0 14a4 4 0 1 1 0-8 4 4 0 0 1 0 8z"/></svg>
      <span>2971 Maplewood Ln, Larkmoor GA 30999</span>
    </p>
  </section>
</body>
</html>
```